Quillon Energy Business Cards

I would like to design some options for about 10 sets of double sided business cards for our team with a raised logo with a Silver glossy finished logo. We are a privately funded upstream Oil & Gas producer drilling vertical wells in Central Oklahoma with a long term production (ROI driven) strategy that we implement through an annual drilling program. We are focused on a shallow / vertical / long life / low decline strategy. We are based in downtown Tulsa Oklahoma. I have attached a sample business card and a picture of our hallway logo which we would like to replicate on the business cards.

Target Market(s)

BRQ Accredited Investors and other Oil & Gas Operators

Industry/Entity Type

Upstream Oil & Gas

Contact Information for Business Card

You can see the sample photo attached, but email / website / address / direct phone / Cell Phone / Name / Title / Fax

Font styles to use
Other font styles liked:
• Felix Titling

Colors
0054AA
0677BA
7BADD7
CADEEF
E8F1F8

Requirements
Must have
• Glossy raised logo
Nice to have
• Possibly a new logo.
Should not have
• No Greens /

```html
<!DOCTYPE html>
<html lang="en">
<head>
<meta charset="utf-8">
<title>Quillon Energy Business Cards</title>
<link rel="stylesheet" href="https://fonts.googleapis.com/css2?family=Montserrat:wght@400;600&display=swap">
<style>
  :root {
    --backdrop: #3b3b3c;
    --card: #1f1f20;
    --silver: #d9d9d9;
    --silver-soft: #bdbdbd;
    --rule: #a9a9a9;
  }
  html, body {
    margin: 0;
    padding: 0;
    width: 1200px;
    height: 1200px;
    overflow: hidden;
    background: var(--backdrop);
    font-family: "Montserrat", Arial, sans-serif;
    color: var(--silver);
  }
  .sheet {
    position: relative;
    width: 1200px;
    height: 1200px;
  }
  .card {
    position: absolute;
    left: 160px;
    width: 880px;
    height: 503px;
    background: var(--card);
    border-radius: 36px;
    box-shadow: 0 18px 40px rgba(0,0,0,0.45);
    overflow: hidden;
  }
  .card--front { top: 70px; }
  .card--back { top: 627px; }

  .wordmark {
    display: flex;
    align-items: center;
    justify-content: center;
    gap: 16px;
    font-weight: 600;
    color: var(--silver);
    letter-spacing: 0.08em;
    text-transform: uppercase;
    white-space: nowrap;
  }
  .wordmark__dot {
    border-radius: 50%;
    background: var(--silver);
    flex: none;
  }
  .card--front .wordmark {
    position: absolute;
    top: 70px;
    left: 0;
    right: 0;
    font-size: 34px;
  }
  .card--front .wordmark__dot { width: 22px; height: 22px; }

  .card--back .wordmark {
    position: absolute;
    inset: 0;
    font-size: 48px;
  }
  .card--back .wordmark__dot { width: 30px; height: 30px; }

  .divider {
    position: absolute;
    height: 2px;
    background: var(--rule);
  }
  .divider--top { left: 300px; right: 60px; top: 178px; }
  .divider--name { left: 60px; width: 380px; top: 290px; }

  .person {
    position: absolute;
    left: 60px;
    top: 212px;
    width: 400px;
    white-space: nowrap;
  }
  .person__name {
    font-size: 24px;
    font-weight: 600;
    letter-spacing: 0.02em;
    margin: 0;
  }
  .person__title {
    font-size: 18px;
    font-weight: 400;
    color: var(--silver-soft);
    letter-spacing: 0.04em;
    margin: 6px 0 0;
  }

  .contact-list {
    position: absolute;
    list-style: none;
    margin: 0;
    padding: 0;
    white-space: nowrap;
  }
  .contact-list--phones { left: 60px; top: 314px; }
  .contact-list--details { left: 490px; top: 206px; }
  .contact-list li {
    display: flex;
    align-items: flex-start;
    gap: 12px;
    font-size: 21px;
    line-height: 1.15;
    margin-bottom: 18px;
    letter-spacing: 0.02em;
  }
  .contact-list--details li { margin-bottom: 16px; }
  .icon {
    width: 24px;
    height: 24px;
    flex: none;
    margin-top: 1px;
    fill: none;
    stroke: var(--silver);
    stroke-width: 1.8;
    stroke-linecap: round;
    stroke-linejoin: round;
  }
  .icon--solid { fill: var(--silver); stroke: none; }
</style>
</head>
<body>
<main class="sheet">

  <section class="card card--front" aria-label="Business card front">
    <div class="wordmark"><span class="wordmark__dot"></span>Quillon Energy, LLC</div>
    <div class="divider divider--top"></div>

    <div class="person">
      <p class="person__name">DORIAN K. VALCOURT, CPL</p>
      <p class="person__title">EXECUTIVE VICE PRESIDENT</p>
    </div>
    <div class="divider divider--name"></div>

    <ul class="contact-list contact-list--phones">
      <li>
        <svg class="icon icon--solid" viewBox="0 0 24 24" aria-hidden="true"><path d="M6.6 10.8a15.1 15.1 0 0 0 6.6 6.6l2.2-2.2a1 1 0 0 1 1-.25 11.4 11.4 0 0 0 3.6.57 1 1 0 0 1 1 1V20a1 1 0 0 1-1 1A17 17 0 0 1 3 4a1 1 0 0 1 1-1h3.5a1 1 0 0 1 1 1c0 1.25.2 2.45.57 3.57a1 1 0 0 1-.25 1z"/></svg>
        539-555-0148
      </li>
      <li>
        <svg class="icon" viewBox="0 0 24 24" aria-hidden="true"><rect x="6" y="2" width="12" height="20" rx="2"/><line x1="11" y1="18" x2="13" y2="18"/></svg>
        918-555-0173
      </li>
      <li>
        <svg class="icon" viewBox="0 0 24 24" aria-hidden="true"><rect x="3" y="9" width="18" height="12" rx="1.5"/><rect x="7" y="3" width="10" height="6"/><line x1="7" y1="13" x2="9" y2="13"/><line x1="11" y1="13" x2="13" y2="13"/><line x1="15" y1="13" x2="17" y2="13"/><line x1="7" y1="17" x2="9" y2="17"/><line x1="11" y1="17" x2="13" y2="17"/><line x1="15" y1="17" x2="17" y2="17"/></svg>
        918-555-0192
      </li>
    </ul>

    <ul class="contact-list contact-list--details">
      <li>
        <svg class="icon" viewBox="0 0 24 24" aria-hidden="true"><rect x="2" y="5" width="20" height="14" rx="1"/><polyline points="2,5 12,13 22,5"/></svg>
        DKV@QETulsa.com
      </li>
      <li>
        <svg class="icon" viewBox="0 0 24 24" aria-hidden="true"><circle cx="12" cy="12" r="10"/><ellipse cx="12" cy="12" rx="4.5" ry="10"/><line x1="2" y1="12" x2="22" y2="12"/><path d="M4 7h16M4 17h16"/></svg>
        www.quillonEnergyLLC.com
      </li>
      <li>
        <svg class="icon" viewBox="0 0 24 24" aria-hidden="true"><path d="M12 22s7-7.2 7-12.5A7 7 0 0 0 5 9.5C5 14.8 12 22 12 22z"/><circle cx="12" cy="9.5" r="2.5"/></svg>
        <span>482 North Boston Ave.<br>Suite 900 Tulsa, OK 74103</span>
      </li>
    </ul>
  </section>

  <section class="card card--back" aria-label="Business card back">
    <div class="wordmark"><span class="wordmark__dot"></span>Quillon Energy, LLC</div>
  </section>

</main>
</body>
</html>
```